Land Buying Company Needs Letterhead for Direct Mail Marketing to Land Owners

We are looking for a professional letterhead that we will be including in our direct mail marketing. We will be sending this to land owners who may be interested in selling or purchasing land.

The letterhead needs to be editable. Headers and footers would look nice, but we are open. We would want it to include our address, website, phone, and email info. For right now the address to use for design purposes would the following:

Address: 415 Bramwell Avenue #600
Dallas, TX 75219
Website - www.quillridgeacres.example
Email - info@quillridgeacres.example
Phone - 866-402-ACRE

I have attached our logo zip file that we just had done on Pixel Guild. Let me know what questions you have, and thank you.

```html
<!DOCTYPE html>
<html lang="en">
<head>
<meta charset="utf-8">
<title>Quill Ridge Acres — Letterhead</title>
<link rel="stylesheet" href="https://fonts.googleapis.com/css2?family=Didact+Gothic&display=swap">
<style>
  :root {
    --backdrop: #c8c8c8;
    --paper: #ffffff;
    --leaf: #99c93b;
    --leaf-pale: #bfdf8a;
    --leaf-mid: #6f9a34;
    --forest: #41591d;
    --ink: #5a5a5a;
    --icon: #6b6b6b;
  }
  * { margin: 0; padding: 0; box-sizing: border-box; }
  html, body {
    width: 1200px; height: 817px; overflow: hidden;
    background: var(--backdrop);
    font-family: "Didact Gothic", "Century Gothic", sans-serif;
  }
  .letterhead {
    position: absolute; left: 340px; top: 41px;
    width: 520px; height: 735px;
    background: var(--paper);
    box-shadow: 0 6px 24px rgba(0,0,0,.25);
    overflow: hidden;
  }
  .letterhead__art { position: absolute; inset: 0; width: 100%; height: 100%; }
  .header-pattern {
    position: absolute; left: 326px; top: 14px;
    width: 194px; height: 132px;
    background: linear-gradient(135deg, var(--leaf-pale) 0%, var(--leaf) 45%, var(--forest) 100%);
    opacity: .9;
  }
  .brand {
    position: absolute; left: 82px; top: 192px;
    font-size: 24px; letter-spacing: 1px;
    color: var(--leaf);
    text-transform: uppercase;
    white-space: nowrap;
  }
  .contact {
    position: absolute; right: 62px; top: 588px;
    list-style: none; text-align: right;
    font-size: 11.5px; color: var(--ink);
    white-space: nowrap;
  }
  .contact li { height: 30px; line-height: 24px; }
</style>
</head>
<body>
  <main class="letterhead">
    <div class="header-pattern" role="img" aria-label="Decorative block of green square tiles in three shades"></div>

    <svg class="letterhead__art" viewBox="0 0 520 735" aria-hidden="true">
      <!-- left band -->
      <path d="M0 150 H40 V360 L0 440 Z" fill="var(--leaf)"/>
      <circle cx="46" cy="204" r="32" fill="var(--paper)"/>
      <circle cx="46" cy="204" r="25" fill="var(--forest)"/>
      <!-- footer band -->
      <path d="M440 552 L520 536 V735 H500 L470 700 Z" fill="var(--leaf)"/>
      <g class="contact-icons">
        <circle cx="474" cy="600" r="11" fill="var(--paper)" stroke="var(--leaf)" stroke-width="1.5"/>
        <path d="M468 597 q6 8 12 6 l-1 -3 -3 1 q-3 -2 -4 -5 l1 -3 -3 -1 z" fill="var(--icon)"/>
        <circle cx="474" cy="630" r="11" fill="var(--paper)" stroke="var(--leaf)" stroke-width="1.5"/>
        <path d="M474 637 l-5 -8 a5 5 0 1 1 10 0 z" fill="var(--icon)"/>
        <circle cx="474" cy="627" r="1.8" fill="var(--paper)"/>
        <circle cx="474" cy="660" r="11" fill="var(--paper)" stroke="var(--leaf)" stroke-width="1.5"/>
        <circle cx="474" cy="660" r="6" fill="none" stroke="var(--icon)" stroke-width="1.5"/>
        <path d="M468 660 h12 M474 654 v12" stroke="var(--icon)" stroke-width="1.2"/>
        <circle cx="474" cy="690" r="11" fill="var(--paper)" stroke="var(--leaf)" stroke-width="1.5"/>
        <rect x="467" y="685" width="14" height="10" fill="var(--icon)"/>
        <path d="M467 685 l7 6 7 -6" fill="none" stroke="var(--paper)" stroke-width="1.2"/>
      </g>
    </svg>

    <svg class="letterhead__art" viewBox="0 0 520 735">
      <defs>
        <linearGradient id="accent-fade" x1="0" y1="0" x2="1" y2="0">
          <stop offset="0" stop-color="var(--leaf)"/>
          <stop offset="1" stop-color="var(--forest)"/>
        </linearGradient>
      </defs>
      <path role="img" aria-label="Diagonal green accent stripes on the left edge"
            d="M0 452 L46 362 L80 362 L0 520 Z" fill="url(#accent-fade)" opacity=".85"/>
      <path role="img" aria-label="Diagonal green accent stripes above the footer band"
            d="M380 520 L520 490 V525 L422 545 Z" fill="url(#accent-fade)" opacity=".85"/>
    </svg>

    <div class="brand">Quill Ridge Acres</div>

    <ul class="contact">
      <li>866-402-ACRE</li>
      <li>415 Bramwell Avenue #600, Dallas, TX 75219</li>
      <li>www.quillridgeacres.example</li>
      <li>info@quillridgeacres.example</li>
    </ul>
  </main>
</body>
</html>
```